Anzeigengestaltung für Sanitätshaus mit orthopädischer Werkstatt
Zielgruppe
Wir sind ein Sanitätshaus mit orthopädischer Werkstatt. Unsere Firma versorgt Patienten von 2-100 Jahren mit Medizinprodukten. Diese sind z.B. Bandagen, Orthesen, Prothesen, Kompressionsstrümpfe...aber auch Pflegebetten, Rollstühle, Toilettenstühle für ältere pflegebedürftige Patienten. Für die letzteren Hilfsmittel suchen wir einen möglichst jungen (20-40 Jahre) Außendienst. Dieser sollte vielleicht einen medizinischen Beruf gelernt haben. Ist aber kein Zwang. Auf jeden Fall sollte er handwerklich begabt sein. Es muß ein offener, freundicher Mensch mit positiver Ausstrahlung sein der offen ist für neue Aufgaben! Die Arbeit ist sehr abwechslungsreich. Eine Weiterbildung (Dauer 2 Tage im Schulungszentrum) zum Mediziprodukteberater und zahlreiche weitere Schulungen über Hilfsmittel, werden dem neuen Mitarbeiter als Grundlage zur Ausübung des Berufes zur Verfügung gestellt. Der Mitarbeiter fährt nach der ausgiebigen Einarbeitungszeit selbstständig mit unserem Lieferwagen zu Partienten, Pflegediensten, Krankenhäuser und liefert dort Reha-Hilfsmittel aus oder past Medizinprodukte an.
Aufgabenstellung
Im Anhang lade ich unsere jetzige, selbst verfasste Anzeige mit dem Logo von unserer Firma. Wir möchten unsere 'Stellenanzeige' bei Quasselhof, Blinkpost und Lumatok laden. Um diese Anzeige auf diesen Kanälen schalten zu können, müssen diese quadratisch sein.
Wichtig ist! Der Text zur Anzeige soll nicht verändert werden.
Ich habe noch ein tolles Bild was bei Pixavera gelistet ist für diese Anzeige:
https://bilder.pixavera-beispiel.de/de/search?serie_id=918346071&asset_id=918346071

```html
<!DOCTYPE html>
<html lang="de">
<head>
<meta charset="utf-8">
<title>Stellenanzeige Reha-Außendienstler</title>
<link rel="stylesheet" href="https://fonts.googleapis.com/css2?family=Roboto+Condensed:wght@300;400;700&display=swap">
<style>
  :root {
    --brand-red: #d31f3c;
    --text-dark: #2b2b2b;
    --frame-grey: #8a8a8a;
    --band-grey: #e9e9e9;
    --logo-grey: #7d7d7d;
    --white: #ffffff;
    --photo-a: #c9d8de;
    --photo-b: #e8e4dc;
    --photo-c: #b4705a;
  }
  html, body {
    margin: 0;
    padding: 0;
    width: 1200px;
    height: 1200px;
    overflow: hidden;
    background: var(--white);
  }
  .ad {
    position: relative;
    width: 1200px;
    height: 1200px;
    font-family: "Roboto Condensed", "Arial Narrow", sans-serif;
    color: var(--text-dark);
  }
  .ad-frame {
    position: absolute;
    left: 24px; top: 24px;
    width: 1150px; height: 1152px;
    border: 2px solid var(--frame-grey);
    box-sizing: border-box;
  }
  .hero-photo {
    position: absolute;
    left: 576px; top: 26px;
    width: 596px; height: 502px;
    background:
      linear-gradient(160deg, var(--photo-a) 0%, var(--photo-b) 55%, var(--photo-c) 100%);
  }
  .headline {
    position: absolute;
    left: 64px; top: 62px;
    width: 500px;
    margin: 0;
    font-weight: 700;
    font-size: 42px;
    line-height: 46px;
    color: var(--brand-red);
  }
  .intro {
    position: absolute;
    left: 64px; top: 286px;
    width: 480px;
    margin: 0;
    font-weight: 300;
    font-size: 23.5px;
    line-height: 30px;
  }
  .info-column {
    position: absolute;
    top: 572px;
    width: 340px;
  }
  .info-column.profile { left: 62px; }
  .info-column.tasks { left: 440px; }
  .info-column.offer { left: 812px; }
  .info-column h2 {
    margin: 0 0 16px;
    font-weight: 400;
    font-size: 24px;
    line-height: 30px;
    text-transform: uppercase;
  }
  .info-column ul {
    list-style: none;
    margin: 0;
    padding: 0;
  }
  .info-column li {
    position: relative;
    padding-left: 12px;
    margin-bottom: 12px;
    font-weight: 300;
    font-size: 23.5px;
    line-height: 36px;
  }
  .info-column li::before {
    content: "";
    position: absolute;
    left: 0; top: 17px;
    width: 3px; height: 3px;
    background: var(--text-dark);
  }
  .footer-band {
    position: absolute;
    left: 26px; top: 1018px;
    width: 1146px; height: 156px;
    background: var(--band-grey);
  }
  .company-name {
    position: absolute;
    left: 74px; top: 1050px;
    width: 280px;
    margin: 0;
    font-weight: 700;
    font-size: 36px;
    line-height: 40px;
    color: var(--logo-grey);
    text-transform: uppercase;
  }
  .apply-box {
    position: absolute;
    left: 410px; top: 1034px;
    width: 716px; height: 124px;
    box-sizing: border-box;
    padding: 14px 24px;
    background: var(--brand-red);
    border-radius: 14px;
    color: var(--white);
    font-weight: 700;
    font-size: 23.5px;
    line-height: 32px;
  }
  .apply-box p { margin: 0; }
  .apply-box .note { font-weight: 300; }
</style>
</head>
<body>
<div class="ad">
  <div class="ad-frame"></div>

  <div class="hero-photo" role="img" aria-label="Foto: junger Mann schiebt fröhlichen älteren Herrn im Rollstuhl durch ein helles Zimmer"></div>

  <h1 class="headline">Junger, dynamischer<br>Reha-Außendienstler /<br>Medizinprodukteberater<br>gesucht!</h1>

  <p class="intro">Unser Familienunternehmen „Sanitätshaus &amp; orthopädische Werkstatt Hollerbach“ versorgt Menschen mit medizinischen Hilfsmitteln und Produkten für Gesundheit und Wohlbefinden. Wir bieten zukunftssichere und abwechs&shy;lungsreiche Tätigkeiten mit hervorragenden Perspektiven im Gesundheitswesen.</p>

  <section class="info-column profile">
    <h2>Ihr Profil:</h2>
    <ul>
      <li>erfolgreich abgeschlossene Berufsausbildung in einem (möglichst) medizinischen Beruf</li>
      <li>zuverlässig, zielstrebig, verant&shy;wortungsbewusst, teamfähig, soziale Kompetenz</li>
      <li>selbstständiges Arbeiten, gute handwerkliche Fähigkeiten</li>
    </ul>
  </section>

  <section class="info-column tasks">
    <h2>Ihre Aufgaben:</h2>
    <ul>
      <li>Auslieferung von Rollstühlen, Rollatoren, Krankenbetten und weiteren Reha-Hilfsmitteln</li>
      <li>Betreuung und Beratung von Kliniken, Pflegediensten, Pflege&shy;heimen und privaten Patienten im Außendienst</li>
      <li>Reparaturen und Anpassungen von Reha-Hilfsmitteln in der Werkstatt</li>
    </ul>
  </section>

  <section class="info-column offer">
    <h2>Unser Angebot:</h2>
    <ul>
      <li>zukunftssicherer Arbeitsplatz 40 Stunden/Woche (Mo – Fr)</li>
      <li>individuelle Einarbeitung mit fortlaufenden Qualifikationen</li>
      <li>Ausbildung zu Medizinproduk&shy;teberater</li>
      <li>gutes Arbeitsklima im Familien&shy;unternehmen</li>
    </ul>
  </section>

  <div class="footer-band"></div>
  <p class="company-name">Sanitätshaus Hollerbach</p>

  <div class="apply-box">
    <p>Überzeugen Sie uns durch Ihre aussagekräftige Bewerbung!</p>
    <p>Senden Sie dies an: info@sani-beispiel.de <span class="note">(Anhänge bitte als PDF)</span> oder</p>
    <p>Sanitätshaus Hollerbach GmbH, Talweg 12, 09999 Musterau</p>
  </div>
</div>
</body>
</html>
```